Infographic about product packaging for aged care

We need an infographic that will be published in Kestrel Magazine, to illustrate some points alongside our Aged Care feature.

Vector style preferred. Please incorporate bright blue and yellow into the colour scheme (Blue: 79C/28M/0Y/0K, Yellow: C5/M2/Y100/K0). Feel free to use other colours to supplement this palette.

Please use the image attached to this brief as a guide to colour and style. This is the opening page of the article.

Dimensions: 102mm x 102mm

Content:
- One in two Australians face difficulty opening or reading packaging
- 53 percent have suffered an injury as a result of inaccessible packaging.
- One in two people face at least one form of restriction:
o sensory (vision, hearing, taste)
o motion (strength, dexterity, locomotion, reach & stretch)
o cognitive (communication & understanding, intellectual functioning)

```html
<!DOCTYPE html>
<html lang="en">
<head>
<meta charset="utf-8">
<title>Packaging accessibility infographic</title>
<link rel="stylesheet" href="https://fonts.googleapis.com/css2?family=Quicksand:wght@500;600&family=Exo+2:wght@600;700&display=swap">
<style>
  :root {
    --bg: #f3f5f5;
    --blue: #0094d6;
    --yellow: #f7e600;
    --ink: #1b1b1b;
  }
  html, body { margin: 0; padding: 0; overflow: hidden; }
  body { width: 1200px; height: 1200px; background: var(--bg); position: relative; font-family: "Quicksand", sans-serif; color: var(--ink); }
  .stat-people-icon {
    position: absolute; left: 258px; top: 126px; width: 228px; height: 140px;
    border-radius: 10px;
    background: linear-gradient(90deg, var(--blue) 0 33%, var(--yellow) 33% 100%);
  }
  .stat-ring { position: absolute; left: 690px; top: 62px; width: 224px; height: 224px; }
  .stat-caption {
    position: absolute; width: 480px; margin: 0; text-align: center;
    font-size: 33px; font-weight: 500; line-height: 41px; letter-spacing: 0.3px;
  }
  .stat-caption.people { left: 117px; top: 295px; }
  .stat-caption.injury { left: 596px; top: 295px; }
  .restriction-intro {
    position: absolute; left: 300px; top: 513px; width: 600px; margin: 0;
    text-align: center; font-size: 33px; font-weight: 500; line-height: 40px;
  }
  .restriction-card {
    position: absolute; top: 632px; width: 263px; height: 532px; background: var(--blue);
    color: var(--yellow); font-family: "Exo 2", sans-serif; text-align: center;
  }
  .restriction-card.sensory { left: 163px; }
  .restriction-card.motion { left: 467px; }
  .restriction-card.cognitive { left: 774px; }
  .card-title { margin: 37px 0 0; font-size: 33px; font-weight: 600; letter-spacing: 0.5px; }
  .card-icon {
    display: block; width: 108px; height: 108px; margin: 40px auto 0;
    border-radius: 14px; background: var(--yellow);
  }
  .card-list { list-style: none; margin: 40px 0 0; padding: 0; font-size: 29.5px; font-weight: 700; line-height: 48px; }
</style>
</head>
<body>
  <div class="stat-people-icon" role="img" aria-label="Pictogram of three standing people, one blue and two yellow"></div>
  <p class="stat-caption people">One in two Australians<br>face difficulty opening<br>or reading packaging</p>

  <svg class="stat-ring" viewBox="0 0 224 224" aria-label="53 percent ring chart">
    <circle cx="112" cy="112" r="92" fill="none" stroke="var(--blue)" stroke-width="3"/>
    <path d="M112 204 A92 92 0 1 1 129.2 21.6" fill="none" stroke="var(--blue)" stroke-width="24" stroke-linecap="round"/>
    <text x="112" y="130" text-anchor="middle" font-family="Exo 2, sans-serif" font-weight="700" font-size="53" fill="var(--blue)">53%</text>
  </svg>
  <p class="stat-caption injury">have suffered an<br>injury as a result of<br>inaccessible packaging.</p>

  <p class="restriction-intro">One in two people face at least<br>one form of restriction :</p>

  <section class="restriction-card sensory">
    <h2 class="card-title">SENSORY</h2>
    <div class="card-icon" role="img" aria-label="Icon of a pointing hand touching"></div>
    <ul class="card-list"><li>vision</li><li>hearing</li><li>taste</li></ul>
  </section>

  <section class="restriction-card motion">
    <h2 class="card-title">MOTION</h2>
    <div class="card-icon" role="img" aria-label="Icon of overlapping squares suggesting movement"></div>
    <ul class="card-list"><li>strength</li><li>desterity</li><li>locomotion</li><li>reach</li><li>stretch</li></ul>
  </section>

  <section class="restriction-card cognitive">
    <h2 class="card-title">COGNITIVE</h2>
    <div class="card-icon" role="img" aria-label="Outline icon of a brain"></div>
    <ul class="card-list"><li>communication</li><li>understanding</li><li>intellectual</li><li>functioning</li></ul>
  </section>
</body>
</html>
```